I need a business card designed using the logo provided either vertical or horizontal......Brenlowe Advisory is an Australian based real estate company that caters for the upper end of the market so the design of the business card "must reflect" the companies image!!
Colour combinations are optional but "must be realistic" and must be able to be accurately useable CMYK colours.
Please consider that any colours used "must be able to be used" and be suitable in following designs for "pull out banner signs" and "real estate signs".
The colours and the font in the attached designs are for example and other combinations are encouraged.
Target Market(s)
The High End of the Australian real estate market
Industry/Entity Type
Business
Contact Information for Business Card
Logo - Business Name - Director + Licensed Real Estate Agent - Mobile Number (Cell Phone) - Business Number - Fax - Email Address - Web address
Requirements
Must have
- Designs and colours (CMYK) that can easily be interpreted by an Australian printer.
Nice to have
- Some alternative ideas on colour and font..........the ones provided are ok and have been provided as an example but I am looking for alternative ideas
Should not have
- Loud, overly bright colours. Designs that do not reflect the professional standards of the business.
- Designs that look good on a computer monitor but can not be re-created on a printing press.............this is most important when it comes to shading etc.

```html
<!DOCTYPE html>
<html lang="en">
<head>
<meta charset="utf-8">
<title>Brenlowe Advisory — Business Card</title>
<link rel="stylesheet" href="https://fonts.googleapis.com/css2?family=Lato:wght@400;700&display=swap">
<style>
  :root {
    --backdrop: #2e2826;
    --card-black: #0b0b0b;
    --card-grey: #5d5f61;
    --cream: #ece3c8;
    --gold: #c99a3e;
    --rule: #9c8a60;
  }
  html, body {
    margin: 0;
    padding: 0;
    width: 1200px;
    height: 844px;
    overflow: hidden;
    background: var(--backdrop);
    font-family: "Lato", "Helvetica Neue", Arial, sans-serif;
  }
  .stage {
    width: 1200px;
    height: 844px;
    display: flex;
    align-items: center;
    justify-content: center;
    gap: 60px;
  }
  .card {
    width: 520px;
    height: 298px;
    box-sizing: border-box;
    position: relative;
  }
  .card--back {
    background: var(--card-black);
    padding: 44px 40px 30px 190px;
    display: flex;
    flex-direction: column;
  }
  .card--front {
    background: var(--card-grey);
    display: flex;
    align-items: center;
    justify-content: center;
  }
  .holder-name {
    margin: 0;
    color: var(--cream);
    font-size: 19px;
    font-weight: 400;
    letter-spacing: 0.5px;
    text-transform: uppercase;
    padding-bottom: 4px;
    border-bottom: 1px solid var(--rule);
    width: 185px;
  }
  .holder-role {
    margin: 5px 0 0 26px;
    color: var(--gold);
    font-size: 15px;
  }
  .contact-list {
    list-style: none;
    margin: 30px 0 0 0;
    padding: 0;
    color: var(--gold);
    font-size: 14px;
    line-height: 19px;
    text-align: right;
    width: 230px;
  }
  .address {
    margin: auto 0 0 -120px;
    color: var(--cream);
    font-size: 13px;
    letter-spacing: 0.2px;
  }
  .brand-name {
    display: flex;
    align-items: center;
    gap: 14px;
    margin-top: -30px;
    color: var(--cream);
    font-size: 30px;
    font-weight: 400;
    letter-spacing: 2px;
    text-transform: uppercase;
  }
  .brand-mark {
    width: 14px;
    height: 14px;
    background: var(--cream);
  }
</style>
</head>
<body>
  <main class="stage">
    <section class="card card--back" aria-label="Business card, contact side">
      <h1 class="holder-name">Marcus Ellery</h1>
      <p class="holder-role">Managing Director</p>
      <ul class="contact-list">
        <li>044-612-3408</li>
        <li>123-784-2051</li>
        <li>hello@brenloweadvisory.com</li>
        <li>www.brenloweadvisory.com</li>
      </ul>
      <p class="address">48 Harbour Crescent | Sydney, NSW | 2000</p>
    </section>
    <section class="card card--front" aria-label="Business card, brand side">
      <div class="brand-name">
        <span class="brand-mark"></span>
        <span>Brenlowe Advisory</span>
      </div>
    </section>
  </main>
</body>
</html>
```